BRIARFELL Real Estate
Real Estate Developer
Project: BRIARFELL Real Estate
BRIARFELL Real Estate - Real Estate
Creative Brief
Use specific fonts
Up to the designer!
Professional
Matthias L. Halvik
Managing Director
BRIARFELL Real Estate GmbH & Co. KG Lindauer Gang 14 20417 Hamburg Germany
mlh@briarfellre.com
briarfellre.com
One-sided or two-sided cards are welcome and any of the three logos and its colour variations can be chosen!

```html
<!DOCTYPE html>
<html lang="de">
<head>
<meta charset="utf-8">
<title>BRIARFELL Real Estate – Business Card</title>
<link rel="stylesheet" href="https://fonts.googleapis.com/css2?family=Arimo:wght@400;700&display=swap">
<style>
  :root{
    --bg:#e4e5e6;
    --green:#2f5b3f;
    --green-dark:#24482f;
    --ink:#3a3d3f;
    --ink-soft:#5a5e61;
    --paper:#ffffff;
    --silver-light:#f4f5f5;
    --silver-mid:#d9dbdc;
    --silver-dark:#b9bcbe;
  }
  *{box-sizing:border-box;margin:0;padding:0}
  html,body{width:1200px;height:871px;overflow:hidden}
  body{background:var(--bg);font-family:"Arimo",Arial,sans-serif;color:var(--ink);
    display:flex;flex-direction:column;align-items:center;justify-content:center;gap:56px}
  .card{width:600px;height:343px;border-radius:16px;position:relative;overflow:hidden;
    box-shadow:0 6px 18px rgba(0,0,0,.18)}

  /* back side */
  .card-back{background:linear-gradient(120deg,var(--silver-light) 0%,var(--silver-mid) 55%,var(--silver-dark) 100%)}
  .back-mark{position:absolute;left:50%;top:50%;transform:translate(-50%,-50%);
    display:flex;flex-direction:column;align-items:center;gap:18px}
  .back-mark .disc{width:150px;height:150px;border-radius:50%;background:var(--green);opacity:.85}
  .back-mark .wordmark{font-weight:700;font-size:30px;letter-spacing:2px;color:var(--green)}

  /* front side */
  .card-front{background:var(--paper)}
  .logo{position:absolute;left:44px;top:82px;width:250px;display:flex;flex-direction:column;align-items:center;gap:12px}
  .logo .disc{width:54px;height:54px;border-radius:50%;background:var(--green)}
  .logo .wordmark{font-weight:700;font-size:34px;line-height:1.05;color:var(--green);text-align:center;letter-spacing:.5px}
  .logo .wordmark span{display:block;font-size:17px;letter-spacing:5px}

  .contact{position:absolute;left:318px;top:56px;font-size:13px;color:var(--ink-soft);line-height:1.45}
  .contact .name{font-size:19px;font-weight:700;color:var(--green-dark);line-height:1.2}
  .contact .role{font-size:13px;font-weight:700;color:var(--ink);margin-bottom:12px}
  .contact .address{margin-bottom:10px}
  .contact ul{list-style:none}
  .contact li{display:flex;align-items:center;gap:9px;height:19px}
  .contact svg{width:13px;height:13px;fill:var(--ink);flex:none}

  .band{position:absolute;left:0;right:0;bottom:0;height:50px;background:var(--green);
    display:flex;align-items:center;padding-left:150px}
  .band .web{color:#fff;font-size:15px;font-weight:700;letter-spacing:3.5px}
</style>
</head>
<body>

<section class="card card-back" aria-label="Card back">
  <div class="back-mark">
    <div class="disc"></div>
    <div class="wordmark">BRIARFELL</div>
  </div>
</section>

<section class="card card-front" aria-label="Card front">
  <div class="logo">
    <div class="disc"></div>
    <div class="wordmark">BRIARFELL<span>REAL ESTATE</span></div>
  </div>

  <div class="contact">
    <p class="name">Matthias L. Halvik</p>
    <p class="role">Managing Director</p>
    <p class="address">Lindauer Gang 14<br>20417 Hamburg, Germany</p>
    <ul>
      <li><svg viewBox="0 0 16 16"><path d="M3.5 1 6 3.6 4.7 5.5c.8 2 2.4 3.6 4.4 4.4L11 8.6 14 11l-1.4 3C7 14 2 9 2 3.2z"/></svg>+49 (0)40 5550182</li>
      <li><svg viewBox="0 0 16 16"><path d="M4.5 0h7a1 1 0 0 1 1 1v14a1 1 0 0 1-1 1h-7a1 1 0 0 1-1-1V1a1 1 0 0 1 1-1zm.8 2v10h5.4V2zM8 13a1 1 0 1 0 0 2 1 1 0 0 0 0-2z"/></svg>+49 (0)175 5550934</li>
      <li><svg viewBox="0 0 16 16"><path d="M4 1h6l2 2v3H4zM1 7h14v7H1zm2 2v1h3V9zm0 2v1h3v-1zm8-2a1 1 0 1 0 0 2 1 1 0 0 0 0-2z"/></svg>+49 (0)40 5550183</li>
      <li><svg viewBox="0 0 16 16"><path d="M1 3h14v10H1zm1.5 1.3v.4L8 9l5.5-4.3v-.4z"/></svg>mlh@briarfellre.com</li>
    </ul>
  </div>

  <div class="band"><span class="web">www.briarfellre.com</span></div>
</section>

</body>
</html>
```